U.S. based testing, inspection, and certification (TIC) company needs a new social media design.

We need a social media design primarily for LinkedIn 1200x1200px for our U.S. based company with international capabilities for performing dozens if not hundreds of testing, inspection, and certification (TIC) services. Our primary services include calibration, chemical analysis, consulting engineering, environmental simulation, forensic engineering, materials testing, mechanical testing, and nondestructive testing. Industries we serve are aerospace/aviation, automotive, chemical, commercial properties, construction, consumer products, defense, energy storage, healthcare, insurance/legal, life science, manufacturing, oil & gas, power generation, pulp & paper, and telecommunications. https://veltrolabs.example/

Guideline hex colors (primary, secondary): #29aae2, #0b1f3b

The final design should communicate:
1. Trust, Integrity, and Independence
2. Technical Expertise and Accuracy
3. Efficiency and Speed
4. Value-Added Partnership

We previously used a hexagon design that we would like to part ways from; hexagon examples and KRV logos uploaded.

```html
<!DOCTYPE html>
<html lang="en">
<head>
<meta charset="utf-8">
<title>KRV – Confidence to Certainty</title>
<link href="https://fonts.googleapis.com/css2?family=Arimo:wght@400;700&family=Roboto:wght@500;700&display=swap" rel="stylesheet">
<style>
  :root {
    --primary: #29aae2;
    --navy: #0b1f3b;
    --space-deep: #050a1c;
    --space-mid: #0c2a66;
    --atmosphere: #3f7fc4;
    --cloud: #c9d8ea;
    --white: #ffffff;
  }
  * { margin: 0; padding: 0; box-sizing: border-box; }
  html, body { width: 1200px; height: 1200px; overflow: hidden; background: var(--white); }
  .canvas {
    position: relative;
    width: 1200px;
    height: 1200px;
    overflow: hidden;
    font-family: "Arimo", Arial, sans-serif;
    color: var(--white);
  }
  .hero-visual {
    position: absolute;
    left: 0; top: 0;
    width: 1200px; height: 742px;
    background:
      radial-gradient(ellipse 900px 420px at 900px 760px, var(--cloud) 0%, rgba(150,180,215,0.55) 35%, rgba(63,127,196,0) 70%),
      radial-gradient(ellipse 1300px 520px at 700px 700px, var(--atmosphere) 0%, rgba(12,42,102,0.8) 55%, rgba(5,10,28,0) 85%),
      linear-gradient(180deg, var(--space-deep) 0%, var(--space-mid) 60%, #1d4f93 100%);
  }
  .brand-mark {
    position: absolute;
    left: 80px; top: 52px;
    font-weight: 700;
    font-size: 168px;
    line-height: 1;
    letter-spacing: 4px;
  }
  .brand-name {
    position: absolute;
    left: 82px; top: 194px;
    font-weight: 400;
    font-size: 35px;
    line-height: 1.2;
  }
  .headline {
    position: absolute;
    left: 82px; top: 282px;
    font-weight: 700;
    font-size: 120px;
    line-height: 135px;
    letter-spacing: -0.5px;
  }
  .info-band {
    position: absolute;
    left: 0; top: 742px;
    width: 1200px; height: 458px;
    background: var(--primary);
  }
  .section-label {
    position: absolute;
    left: 0;
    width: 424px; height: 50px;
    background: var(--navy);
    padding-left: 76px;
    font-family: "Roboto", Arial, sans-serif;
    font-weight: 500;
    font-size: 25px;
    line-height: 50px;
  }
  .section-label.services { top: 779px; }
  .section-label.industries { top: 940px; }
  .section-body {
    position: absolute;
    left: 78px;
    width: 1090px;
    font-family: "Roboto", Arial, sans-serif;
    font-weight: 700;
    font-size: 26px;
    line-height: 35px;
    letter-spacing: -0.3px;
  }
  .section-body.services { top: 845px; }
  .section-body.industries { top: 998px; }
  .site-url {
    position: absolute;
    left: 78px; top: 1108px;
    font-family: "Roboto", Arial, sans-serif;
    font-weight: 500;
    font-size: 31px;
    color: var(--navy);
  }
</style>
</head>
<body>
<main class="canvas">
  <div class="hero-visual" role="img" aria-label="Satellite with solar panels orbiting above Earth's cloud-covered atmosphere"></div>

  <div class="brand-mark">KRV</div>
  <div class="brand-name">Kestrel Reliability Ventures</div>

  <h1 class="headline">We take you from<br>confidence to<br>certainty</h1>

  <section class="info-band"></section>

  <h2 class="section-label services">Our primary services</h2>
  <p class="section-body services">calibration, chemical analysis, consulting engineering, environmental simulation, forensic engineering, materials testing, mechanical testing, and nondestructive testing.</p>

  <h2 class="section-label industries">Industries we serve</h2>
  <p class="section-body industries">aerospace/aviation, automotive, chemical, commercial properties, construction, consumer products, defense, energy storage, healthcare, insurance/legal, life science, manufacturing, oil &amp; gas, power generation, pulp &amp; paper, and telecommunications.</p>

  <div class="site-url">https://veltrolabs.example/</div>
</main>
</body>
</html>
```